Mortgage Loan Program(s) for Furloughed Federal Government Workers

Mortgage Loan Program(s)
For
Furloughed Federal Government Workers

* Preserve Your Credit Rating
* Receive Cash out to Increase Savings or Consolidate Bills
* Close in 30 Days or Less
* FHA and Conventional Loan Programs
* Very Competitive Rates Available
* DC & MD Properties Only

You deserve better. Contact us today....

Office (800) 446-2917 x24
Cell (240) 958-2043
Email mpelton@brightkeyhome.example

Marcus Pelton
Brightkey Financial Services, Inc.
NMLS #518374 / #60471

Target Market(s)

```html
<!DOCTYPE html>
<html lang="en">
<head>
<meta charset="utf-8">
<title>Mortgage Loan Programs – Brightkey Financial Services</title>
<link rel="stylesheet" href="https://fonts.googleapis.com/css2?family=Montserrat:wght@400;500;600;700&family=Cabin:wght@400;500&display=swap">
<style>
  :root {
    --page-bg: #e9ecee;
    --teal: #2fbdb0;
    --green: #76c477;
    --green-mid: #5cc08a;
    --ink: #1f3d48;
    --band-dark: rgba(40, 62, 78, 0.62);
    --band-olive: #97a33f;
    --rule: #2b3a45;
    --footer-left: #79c47a;
    --footer-right: #7fd0b1;
    --white: #ffffff;
    --logo-blue: #1d5ea8;
  }
  * { margin: 0; padding: 0; box-sizing: border-box; }
  html, body {
    width: 1200px; height: 1200px; overflow: hidden;
    background: var(--page-bg);
  }
  .flyer {
    position: absolute; left: 0; top: 96px;
    width: 1168px; height: 980px;
    transform: scale(1.02740); transform-origin: top left;
    background: linear-gradient(100deg, var(--teal) 0%, var(--green-mid) 45%, var(--green) 100%);
    overflow: hidden;
    color: var(--ink);
  }
  .flyer__art { position: absolute; inset: 0; }
  .headline {
    position: absolute; left: 44px; top: 30px;
    font: 700 44px/1 "Montserrat", sans-serif; letter-spacing: 0.2px;
  }
  .subhead {
    position: absolute; left: 44px; top: 89px;
    font: 400 25px/1 "Montserrat", sans-serif;
  }
  .benefits { list-style: none; }
  .benefit {
    position: absolute;
    font: 400 28px/36px "Cabin", sans-serif;
    padding-left: 30px;
    white-space: nowrap;
  }
  .benefit svg { position: absolute; left: 0; top: 11px; width: 18px; height: 16px; }
  .tagline {
    position: absolute; left: 32px; top: 790px;
    font: 600 29px/1 "Montserrat", sans-serif;
  }
  .contact {
    position: absolute; left: 38px; top: 882px;
    list-style: none;
    font: 400 15px/23px "Montserrat", sans-serif;
    white-space: nowrap;
  }
  .contact li { display: flex; align-items: center; gap: 12px; }
  .contact svg { width: 16px; height: 16px; flex: none; }
  .divider {
    position: absolute; left: 366px; top: 880px;
    width: 2px; height: 68px; background: var(--rule);
  }
  .agent {
    position: absolute; left: 396px; top: 882px;
    font: 400 15px/23px "Montserrat", sans-serif;
    white-space: nowrap;
  }
  .agent__name { font-weight: 600; }
  .brand {
    position: absolute; left: 943px; top: 846px; width: 225px; height: 134px;
    background: var(--white);
    display: flex; align-items: center; justify-content: center; gap: 10px;
    padding: 0 14px;
  }
  .brand__dot { width: 22px; height: 22px; border-radius: 50%; background: var(--logo-blue); flex: none; }
  .brand__name { font: 600 16px/1.25 "Montserrat", sans-serif; color: var(--logo-blue); }
</style>
</head>
<body>
<main class="flyer">
  <svg class="flyer__art" viewBox="0 0 1168 980" width="1168" height="980">
    <defs>
      <linearGradient id="photoTone" x1="0" y1="0" x2="1" y2="1">
        <stop offset="0" stop-color="#e8e2dc"/>
        <stop offset="0.5" stop-color="#cdb89c"/>
        <stop offset="1" stop-color="#8f7a62"/>
      </linearGradient>
      <linearGradient id="footerTone" x1="0" y1="0" x2="1" y2="0">
        <stop offset="0" stop-color="#79c47a"/>
        <stop offset="1" stop-color="#80d1b3"/>
      </linearGradient>
      <linearGradient id="flagTone" x1="0" y1="0" x2="1" y2="1">
        <stop offset="0" stop-color="#86c9a8"/>
        <stop offset="1" stop-color="#5da88a"/>
      </linearGradient>
    </defs>
    <polygon points="0,164 749,164 527,710 0,710" fill="url(#photoTone)" role="img" aria-label="Photo of a couple reviewing a mortgage application at a table with a small model house"/>
    <polygon points="0,149 705,149 681,208 0,208" fill="var(--band-dark)"/>
    <polygon points="0,694 530,694 507,754 0,754" fill="var(--band-olive)"/>
    <rect x="0" y="846" width="943" height="13" fill="var(--rule)"/>
    <rect x="0" y="859" width="943" height="121" fill="url(#footerTone)"/>
    <rect x="818" y="859" width="125" height="121" fill="url(#flagTone)" role="img" aria-label="Faded waving American flag"/>
  </svg>

  <h1 class="headline">Mortgage Loan Programs</h1>
  <p class="subhead">For Furloughed Federal Government Workers</p>

  <ul class="benefits">
    <li class="benefit" style="left:772px;top:239px"><svg viewBox="0 0 18 16"><path d="M2 8l5 5 9-11" fill="none" stroke="currentColor" stroke-width="3"/></svg>Preserve Your Credit Rating</li>
    <li class="benefit" style="left:745px;top:311px"><svg viewBox="0 0 18 16"><path d="M2 8l5 5 9-11" fill="none" stroke="currentColor" stroke-width="3"/></svg>Receive Cash out to Increase<br>Savings or Consolidate Bills</li>
    <li class="benefit" style="left:707px;top:418px"><svg viewBox="0 0 18 16"><path d="M2 8l5 5 9-11" fill="none" stroke="currentColor" stroke-width="3"/></svg>Close in 30 Days or Less</li>
    <li class="benefit" style="left:682px;top:490px"><svg viewBox="0 0 18 16"><path d="M2 8l5 5 9-11" fill="none" stroke="currentColor" stroke-width="3"/></svg>FHA and Conventional<br>Loan Programs</li>
    <li class="benefit" style="left:643px;top:597px"><svg viewBox="0 0 18 16"><path d="M2 8l5 5 9-11" fill="none" stroke="currentColor" stroke-width="3"/></svg>Very Competitive Rates Available</li>
    <li class="benefit" style="left:617px;top:668px"><svg viewBox="0 0 18 16"><path d="M2 8l5 5 9-11" fill="none" stroke="currentColor" stroke-width="3"/></svg>DC &amp; MD Properties Only</li>
  </ul>

  <p class="tagline">You deserve better. Contact us today....</p>

  <ul class="contact">
    <li><svg viewBox="0 0 16 16"><circle cx="8" cy="8" r="7" fill="var(--ink)"/><path d="M5 4l2 2-1 1.5 2.5 2.5L10 9l2 2-1.5 1.5C8 12 4 8 3.5 5.5z" fill="var(--footer-left)"/></svg>(800) 446-2917 x24</li>
    <li><svg viewBox="0 0 16 16"><circle cx="8" cy="8" r="7" fill="var(--ink)"/><path d="M5 4l2 2-1 1.5 2.5 2.5L10 9l2 2-1.5 1.5C8 12 4 8 3.5 5.5z" fill="var(--footer-left)"/></svg>(240) 958-2043</li>
    <li><svg viewBox="0 0 16 16"><circle cx="8" cy="8" r="7" fill="var(--ink)"/><rect x="4" y="5" width="8" height="6" fill="none" stroke="var(--footer-left)" stroke-width="1.2"/><path d="M4 5l4 3.5L12 5" fill="none" stroke="var(--footer-left)" stroke-width="1.2"/></svg>mpelton@brightkeyhome.example</li>
  </ul>

  <div class="divider"></div>

  <div class="agent">
    <p class="agent__name">Marcus Pelton</p>
    <p>Brightkey Financial Services, Inc.</p>
    <p>NMLS #518374 / #60471</p>
  </div>

  <div class="brand">
    <span class="brand__dot"></span>
    <span class="brand__name">Brightkey Financial Services, Inc.</span>
  </div>
</main>
</body>
</html>
```